Roll Up Design Velumo

We are a beauty company and we need stunning design for our general roll-up banner that we gonna place just next to the main gate of mall that we are located in. The most important for us is the quality, accuracy and the unity of poster. It has to be super elegant, engaging and beautiful. Has to match our service standards (high). Colors do not matter as long as the overall look is exciting.
Examples and our logo are attached
Updates
Reason: We need more designs (more creativity, more quality, colurs and proportions).
Target Market(s)
Middle class ladies, students, business women
Industry/Entity Type
It Company
Colors
Designer to choose colors to be used in the design.
Look and feel
Each slider illustrates characteristics of the customer's brand and the style your logo design should communicate.

```html
<!DOCTYPE html>
<html lang="az">
<head>
<meta charset="utf-8">
<title>Velumo Gözəllik — Roll-up</title>
<link href="https://fonts.googleapis.com/css2?family=Roboto+Condensed:wght@400;700&display=swap" rel="stylesheet">
<style>
  :root {
    --brand-red: #c8283a;
    --ink: #141414;
    --white: #ffffff;
    --silk-light: #f4eeec;
    --silk-mid: #e4d6d2;
    --silk-deep: #cbb5ae;
    --skin-light: #f0d3c6;
    --skin: #e2b6a3;
    --skin-deep: #c99483;
  }
  html, body {
    margin: 0;
    padding: 0;
    width: 1200px;
    height: 2857px;
    overflow: hidden;
    background: var(--silk-light);
  }
  .banner {
    position: relative;
    width: 1200px;
    height: 2857px;
    overflow: hidden;
    font-family: "Roboto Condensed", "Arial Narrow", sans-serif;
  }
  .banner__backdrop {
    position: absolute;
    inset: 0;
    background:
      linear-gradient(100deg, var(--silk-mid) 0%, var(--silk-light) 28%, var(--silk-deep) 58%, var(--silk-light) 72%, var(--silk-mid) 100%);
  }
  .banner__portrait {
    position: absolute;
    left: 0;
    top: 1100px;
    width: 900px;
    height: 1757px;
    background:
      radial-gradient(ellipse 260px 190px at 360px 560px, rgba(201,148,131,0.55) 0%, rgba(201,148,131,0) 100%),
      radial-gradient(ellipse 430px 700px at 380px 720px, var(--skin-light) 0%, var(--skin) 45%, rgba(226,182,163,0.7) 70%, rgba(226,182,163,0) 100%),
      radial-gradient(ellipse 560px 900px at 300px 900px, rgba(201,148,131,0.35) 0%, rgba(201,148,131,0) 100%);
  }
  .brand {
    position: absolute;
    top: 62px;
    left: 0;
    width: 1200px;
    text-align: center;
  }
  .brand__name {
    display: block;
    font-weight: 700;
    font-size: 176px;
    line-height: 160px;
    letter-spacing: 16px;
    color: var(--ink);
  }
  .brand__rule {
    width: 512px;
    height: 3px;
    margin: 14px auto 0;
    background: var(--brand-red);
  }
  .brand__descriptor {
    display: block;
    margin-top: 26px;
    font-weight: 400;
    font-size: 54px;
    line-height: 56px;
    letter-spacing: 2px;
    color: var(--brand-red);
  }
  .slogan {
    position: absolute;
    left: 0;
    top: 364px;
    width: 683px;
    height: 274px;
    box-sizing: border-box;
    padding: 20px 0 0 95px;
    background: var(--brand-red);
    color: var(--white);
    font-weight: 700;
    font-size: 104px;
    line-height: 116px;
  }
  .vertical-name {
    position: absolute;
    left: 700px;
    top: 350px;
    width: 400px;
    height: 2120px;
  }
  .web {
    position: absolute;
    left: 60px;
    top: 2545px;
    width: 1080px;
    height: 130px;
  }
  .contact-band {
    position: absolute;
    left: 0;
    bottom: 0;
    width: 1200px;
    height: 160px;
    background: var(--brand-red);
    color: var(--white);
    font-size: 64px;
    line-height: 160px;
    text-align: center;
    white-space: nowrap;
  }
</style>
</head>
<body>
  <main class="banner">
    <div class="banner__backdrop"></div>
    <div class="banner__portrait" role="img" aria-label="Profile portrait of a woman with eyes closed, facing left, soft beauty lighting"></div>

    <header class="brand">
      <span class="brand__name">VELUMO</span>
      <div class="brand__rule"></div>
      <span class="brand__descriptor">GÖZƏLLİK</span>
    </header>

    <div class="slogan">Gözellik her<br>yandadir...</div>

    <svg class="vertical-name" viewBox="0 0 400 2120" aria-hidden="true">
      <text x="0" y="0" transform="translate(360 2100) rotate(-90)"
            font-family="Roboto Condensed, Arial Narrow, sans-serif" font-weight="700"
            font-size="480" fill="#c8283a" fill-opacity="0.92"
            textLength="2080" lengthAdjust="spacingAndGlyphs">VELUMO</text>
    </svg>

    <svg class="web" viewBox="0 0 1080 130" aria-label="www.velumogozellik.com">
      <text x="540" y="100" text-anchor="middle"
            font-family="Roboto Condensed, Arial Narrow, sans-serif" font-weight="700"
            font-size="108" fill="#c8283a"
            textLength="1070" lengthAdjust="spacingAndGlyphs">www.velumogozellik.com</text>
    </svg>

    <footer class="contact-band">office@velumogozellik.com | (012) 555 0142</footer>
  </main>
</body>
</html>
```